Thornwell Accountancy
Business Cards and Stationary Design
Thornwell Accountancy - Financial Services
Creative Brief
Use specific fonts
Open to either the same or different fonts.
Professional
Gareth Lomax
Proprietor
Thornwell Accountancy 17 Hadley Close Marlborough Wiltshire SN8 1QT
gareth@thornwellaccountancy.example.co.uk
www.thornwellaccountancy.example.co.uk
Stationary to include: Business Cards, Letterhead, Generic Headed Paper, Compliments Slip and Envelopes
I would like the business cards and stationary to compliment the colour scheme used in my website. I have attached a number of logos that could potentially be used. At this time I am open to any suggestions and will provide feedback through the contest.
lomaxgary lomaxgary
All designers Would still like to see some more designers entering this contest. Please post designs that compliment the website colour scheme and try not to use the gold logos attach on white backgrounds. Thanks.
All, On envelopes - a logo etc is fine, but please do not show any address information. Thanks.
Hi Vimto42, apologies for last comment, you are already using the colours I like. Could you try a few designs using the burgundy red colour on the back of the card. Thanks
hollowpixels: Having seen the design using the gold & red logo on the white background I think I prefer the silver & gold one. Can you do some designs with that version & also using a slightly darker more burgundy red colour. Thanks
#vimto42: having seen it, I'm not sure about the use of the gold logo on the white background. Could I ask you to also use the darker red found on my website? Can I also see some designs where the back of the card is coloured and the front being patterned as you have shown already?
#hollowpixels: nice designs but I really need to see the full stationary package as well (and double-sided biz cards). Also, could you maybe use the darker red From my website in your colour schemes please? Thanks.
All, please can you use all lower case characters for the email and web addresses. Thanks
Hi all.... I have uploaded some logos that you may wish to use in the design contest. As mentioned in the brief, I would like to see some designs that compliment these logos and my website colour scheme.......but am open to seeing other design concepts to. Thanks...

```html
<!DOCTYPE html>
<html lang="en">
<head>
<meta charset="utf-8">
<title>Thornwell Accountancy Stationery Set</title>
<link href="https://fonts.googleapis.com/css2?family=Cinzel:wght@600&family=Great+Vibes&family=Open+Sans:wght@400&display=swap" rel="stylesheet">
<style>
  :root{
    --burgundy:#6a0e14;
    --red:#8f1b22;
    --silver:#cfcfcf;
    --paper:#ffffff;
    --stage:#f1f1f1;
    --ink:#555555;
    --watermark:#efe6e6;
  }
  html,body{margin:0;padding:0;overflow:hidden}
  body{width:1200px;height:262px;background:var(--stage);position:relative;font-family:"Open Sans",sans-serif}
  .sheet{position:absolute;background:var(--paper);box-shadow:0 1px 3px rgba(0,0,0,.25);overflow:hidden}
  .sheet.dark{background:var(--burgundy)}
  .wave{position:absolute;left:0;bottom:0;width:100%;display:block}
  .brand{position:absolute;left:0;right:0;text-align:center;font-family:"Cinzel",serif;font-weight:600;color:var(--red);line-height:1}
  .brand .dot{display:block;margin:0 auto 2px;border-radius:50%;background:var(--red)}
  .dark .brand{color:var(--paper)}
  .dark .brand .dot{background:var(--paper)}
  .watermark{position:absolute;border-radius:50%;background:radial-gradient(var(--watermark),rgba(239,230,230,0) 70%)}
  .contact{position:absolute;font-size:3px;color:var(--ink);line-height:1.4}
  .letterhead{top:19px;width:134px;height:221px}
  .letterhead .brand{top:12px;font-size:6px}
  .letterhead .brand .dot{width:8px;height:8px}
  .letterhead .watermark{left:22px;top:62px;width:90px;height:90px}
  .letterhead .contact{right:6px;bottom:4px;color:#f3dede;text-align:right}
  .card{left:12px;width:100px;height:56px}
  .card .brand{top:10px;font-size:6px}
  .card .brand .dot{width:7px;height:7px}
  .card .contact{left:6px;bottom:14px}
  .slip{left:804px;width:144px;height:86px}
  .slip .brand{top:6px;font-size:5px}
  .slip .brand .dot{width:6px;height:6px}
  .slip .greeting{position:absolute;left:22px;top:32px;font-family:"Great Vibes",cursive;font-size:12px;color:var(--red)}
  .envelope{left:972px;width:216px;height:58px}
  .envelope .brand{top:8px;left:10px;right:auto;font-size:5px;text-align:left}
  .envelope .brand .dot{width:6px;height:6px;margin:0 0 2px}
  .envelope .flap{position:absolute;inset:0;width:100%;height:100%}
</style>
</head>
<body>

<!-- Business cards -->
<div class="sheet card" style="top:44px">
  <div class="brand"><span class="dot"></span>Thornwell Accountancy</div>
  <div class="contact">Gareth Lomax · Proprietor<br>gareth@thornwellaccountancy.example.co.uk</div>
  <svg class="wave" viewBox="0 0 100 14" preserveAspectRatio="none" height="14"><path d="M0 8 Q40 0 100 6 L100 14 L0 14Z" fill="var(--red)"/><path d="M0 8 Q40 0 100 6" stroke="var(--silver)" stroke-width="1" fill="none"/></svg>
</div>
<div class="sheet card dark" style="top:108px">
  <div class="brand" style="top:18px"><span class="dot"></span>Thornwell Accountancy</div>
  <svg class="wave" viewBox="0 0 100 14" preserveAspectRatio="none" height="14"><path d="M0 6 Q50 14 100 4" stroke="var(--silver)" stroke-width="1" fill="none"/></svg>
</div>
<div class="sheet card" style="top:190px">
  <div class="brand"><span class="dot"></span>Thornwell Accountancy</div>
  <div class="contact">17 Hadley Close Marlborough Wiltshire SN8 1QT<br>www.thornwellaccountancy.example.co.uk</div>
  <svg class="wave" viewBox="0 0 100 14" preserveAspectRatio="none" height="14"><path d="M0 8 Q40 0 100 6 L100 14 L0 14Z" fill="var(--red)"/><path d="M0 8 Q40 0 100 6" stroke="var(--silver)" stroke-width="1" fill="none"/></svg>
</div>

<!-- Letterheads -->
<div class="sheet letterhead" style="left:130px">
  <div class="brand"><span class="dot"></span>Thornwell Accountancy</div>
  <div class="watermark" role="img" aria-label="Faint tree emblem watermark"></div>
  <svg class="wave" viewBox="0 0 100 24" preserveAspectRatio="none" height="24"><path d="M0 12 Q45 2 100 10 L100 24 L0 24Z" fill="var(--burgundy)"/><path d="M0 12 Q45 2 100 10" stroke="var(--silver)" stroke-width="1.2" fill="none"/></svg>
  <div class="contact">17 Hadley Close Marlborough Wiltshire SN8 1QT<br>gareth@thornwellaccountancy.example.co.uk</div>
</div>
<div class="sheet letterhead" style="left:293px">
  <div class="brand"><span class="dot"></span>Thornwell Accountancy</div>
  <div class="watermark" role="img" aria-label="Faint tree emblem watermark"></div>
  <svg class="wave" viewBox="0 0 100 24" preserveAspectRatio="none" height="24"><path d="M0 12 Q45 2 100 10 L100 24 L0 24Z" fill="var(--burgundy)"/><path d="M0 12 Q45 2 100 10" stroke="var(--silver)" stroke-width="1.2" fill="none"/></svg>
  <div class="contact">17 Hadley Close Marlborough Wiltshire SN8 1QT<br>www.thornwellaccountancy.example.co.uk</div>
</div>
<div class="sheet letterhead" style="left:466px">
  <div class="brand"><span class="dot"></span>Thornwell Accountancy</div>
  <div class="watermark" role="img" aria-label="Faint tree emblem watermark"></div>
  <svg class="wave" viewBox="0 0 100 24" preserveAspectRatio="none" height="24"><path d="M0 12 Q45 2 100 10 L100 24 L0 24Z" fill="var(--burgundy)"/><path d="M0 12 Q45 2 100 10" stroke="var(--silver)" stroke-width="1.2" fill="none"/></svg>
</div>
<div class="sheet letterhead" style="left:634px">
  <div class="brand"><span class="dot"></span>Thornwell Accountancy</div>
  <svg class="wave" viewBox="0 0 100 24" preserveAspectRatio="none" height="24"><path d="M0 12 Q45 2 100 10 L100 24 L0 24Z" fill="var(--burgundy)"/><path d="M0 12 Q45 2 100 10" stroke="var(--silver)" stroke-width="1.2" fill="none"/></svg>
</div>

<!-- Compliments slips -->
<div class="sheet slip" style="top:43px">
  <div class="brand"><span class="dot"></span>Thornwell Accountancy</div>
  <div class="greeting">With Compliments</div>
  <svg class="wave" viewBox="0 0 100 16" preserveAspectRatio="none" height="16"><path d="M0 9 Q45 0 100 7 L100 16 L0 16Z" fill="var(--burgundy)"/><path d="M0 9 Q45 0 100 7" stroke="var(--silver)" stroke-width="1" fill="none"/></svg>
</div>
<div class="sheet slip" style="top:156px">
  <div class="brand"><span class="dot"></span>Thornwell Accountancy</div>
  <svg class="wave" viewBox="0 0 100 16" preserveAspectRatio="none" height="16"><path d="M0 9 Q45 0 100 7 L100 16 L0 16Z" fill="var(--burgundy)"/><path d="M0 9 Q45 0 100 7" stroke="var(--silver)" stroke-width="1" fill="none"/></svg>
</div>

<!-- Envelopes -->
<div class="sheet envelope" style="top:77px">
  <div class="brand"><span class="dot"></span>Thornwell Accountancy</div>
  <svg class="wave" viewBox="0 0 100 14" preserveAspectRatio="none" height="14"><path d="M0 9 Q50 0 100 7 L100 14 L0 14Z" fill="var(--burgundy)"/><path d="M0 9 Q50 0 100 7" stroke="var(--silver)" stroke-width="1" fill="none"/></svg>
</div>
<div class="sheet envelope" style="top:168px">
  <svg class="flap" viewBox="0 0 216 58" preserveAspectRatio="none"><path d="M0 0 L108 30 L216 0Z" fill="var(--burgundy)"/><path d="M0 0 L108 30 L216 0" stroke="var(--silver)" stroke-width="1" fill="none"/></svg>
</div>

</body>
</html>
```